Business card design needed

Double sided
Color, unique, elegant

Maybe put this quote somewhere?? But I think it might make it to cluttered?
“The Pilates Method of Body
Conditioning develops the body
uniformly, corrects posture, restores
vitality, invigorates the mind and
elevates the spirit”
- Lionel Hartwick

Industry/Entity Type

Business

Contact Information for Business Card

Marla Trevisick
Pilates Instructor & Personal trainer
Mobile: 0498260543
www.kovira.com.au
email: koviraheal.motion@brintmail.com

```html
<!DOCTYPE html>
<html lang="en">
<head>
<meta charset="utf-8">
<title>Kovira Health and Fitness – Business Card</title>
<link rel="stylesheet" href="https://fonts.googleapis.com/css2?family=Poiret+One&family=Montserrat:wght@600&family=Schoolbell&display=swap">
<style>
  :root {
    --card-bg: #ffffff;
    --ink: #1a1a1a;
    --ink-soft: #3a3a3a;
    --plum: #8e3f90;
    --leaf: #8fcf7a;
  }
  * { margin: 0; padding: 0; box-sizing: border-box; }
  html, body {
    width: 1200px;
    height: 693px;
    overflow: hidden;
    background: var(--card-bg);
  }
  .card {
    position: relative;
    width: 1200px;
    height: 693px;
    background: var(--card-bg);
  }
  .brand-mark {
    position: absolute;
    left: 561px;
    top: 120px;
    width: 96px;
    height: 96px;
  }
  .brand-name {
    position: absolute;
    left: 0;
    width: 100%;
    top: 296px;
    text-align: center;
    font-family: "Poiret One", sans-serif;
    font-size: 64px;
    line-height: 1;
    letter-spacing: 4px;
    color: var(--ink);
  }
  .brand-tagline {
    position: absolute;
    left: 0;
    width: 100%;
    top: 379px;
    text-align: center;
    font-family: "Montserrat", sans-serif;
    font-weight: 600;
    font-size: 21px;
    line-height: 1;
    color: var(--ink);
  }
  .person-name {
    position: absolute;
    left: 0;
    width: 100%;
    top: 440px;
    text-align: center;
    font-family: "Schoolbell", cursive;
    font-size: 46px;
    line-height: 1;
    letter-spacing: 15px;
    color: var(--plum);
  }
  .person-role {
    position: absolute;
    left: 0;
    width: 100%;
    top: 514px;
    text-align: center;
    font-family: "Poiret One", sans-serif;
    font-size: 27px;
    line-height: 35px;
    letter-spacing: 0.5px;
    color: var(--ink-soft);
  }
</style>
</head>
<body>
  <main class="card">
    <svg class="brand-mark" viewBox="0 0 96 96" aria-hidden="true">
      <circle cx="48" cy="48" r="46" fill="var(--leaf)"/>
    </svg>
    <h1 class="brand-name">KOVIRA</h1>
    <p class="brand-tagline">Health and Fitness</p>
    <h2 class="person-name">Marla Trevisick</h2>
    <p class="person-role">Pilates Instructor &amp;<br>Personal Trainer</p>
  </main>
</body>
</html>
```